Zolva Mindfulness Planner is need a great daily page!

We are looking for a desing which would be the base for a new planner series. Our self-help journey lead us to an idea, to put everything into a frame what worked for us over these years. We want to help others to apply all these self help ideas,, tricks and habits in a fun, practical and and dynamic way.
We would like to see designs for the main daily page.
Focusing on letter types, colours, and set the flow of the day.

Low design quality

```html
<!DOCTYPE html>
<html lang="en">
<head>
<meta charset="utf-8">
<title>Zolva Mindfulness Planner – Daily Page</title>
<link href="https://fonts.googleapis.com/css2?family=Montserrat:wght@400;600&family=Pacifico&display=swap" rel="stylesheet">
<style>
  :root {
    --ink: #111111;
    --rule: #555555;
    --navy: #1d2f52;
    --teal: #4d868c;
    --paper: #ffffff;
  }
  * { margin: 0; padding: 0; box-sizing: border-box; }
  html, body { width: 1200px; height: 1200px; overflow: hidden; background: var(--paper); }
  body { position: relative; font-family: "Montserrat", sans-serif; color: var(--ink); }
  .page { position: absolute; top: 235px; width: 511px; height: 729px; border: 1px solid var(--ink); background: var(--paper); }
  .page--weekly { left: 63px; }
  .page--daily { left: 622px; }
  .abs { position: absolute; white-space: nowrap; }
  .title { left: 41px; top: 46px; font-family: "Pacifico", cursive; font-size: 28px; font-weight: 400; line-height: 1; }
  .date-range { top: 37px; font-size: 14px; }
  .band { left: 0; top: 103px; width: 100%; height: 8px; background: var(--navy); }
  .heading { font-size: 17.5px; font-weight: 600; }
  .label { font-size: 14.5px; transform: translateX(-50%); }
  .rule { height: 1px; background: var(--rule); }
  .day-box { left: 271px; width: 207px; height: 101px; border: 1px solid var(--rule); text-align: center; font-size: 14.5px; line-height: 18px; }
  .num { font-size: 14.5px; }
  .slot { left: 34px; width: 208px; height: 38px; background: var(--teal); color: var(--paper); font-size: 14px; padding: 2px 3px; }
  .hour { left: 37px; font-size: 14px; }
</style>
</head>
<body>

<section class="page page--weekly">
  <h1 class="abs title">Weekly Planner</h1>
  <span class="abs date-range" style="left:271px">From</span>
  <span class="abs date-range" style="left:342px">/</span>
  <span class="abs date-range" style="left:382px">To</span>
  <span class="abs date-range" style="left:434px">/</span>
  <div class="abs band"></div>

  <h2 class="abs heading" style="left:35px;top:118px">Start The Day</h2>
  <span class="abs label" style="left:139px;top:160px">Today I am grateful for</span>
  <div class="abs rule" style="left:35px;width:208px;top:209px"></div>
  <div class="abs rule" style="left:35px;width:208px;top:235px"></div>
  <div class="abs rule" style="left:35px;width:208px;top:262px"></div>
  <div class="abs rule" style="left:35px;width:208px;top:289px"></div>
  <div class="abs rule" style="left:35px;width:208px;top:316px"></div>
  <div class="abs rule" style="left:35px;width:208px;top:342px"></div>

  <span class="abs label" style="left:139px;top:390px">My&nbsp; Top 3 Priorities Today</span>
  <span class="abs num" style="left:35px;top:416px">1)</span>
  <div class="abs rule" style="left:35px;width:208px;top:438px"></div>
  <span class="abs num" style="left:35px;top:443px">2)</span>
  <div class="abs rule" style="left:35px;width:208px;top:465px"></div>
  <span class="abs num" style="left:35px;top:471px">3)</span>
  <div class="abs rule" style="left:35px;width:208px;top:493px"></div>

  <span class="abs label" style="left:139px;top:539px">Today I am</span>
  <div class="abs rule" style="left:35px;width:208px;top:586px"></div>
  <div class="abs rule" style="left:35px;width:208px;top:614px"></div>
  <div class="abs rule" style="left:35px;width:208px;top:640px"></div>
  <div class="abs rule" style="left:35px;width:208px;top:666px"></div>
  <div class="abs rule" style="left:35px;width:208px;top:694px"></div>

  <div class="abs day-box" style="top:123px">Monday</div>
  <div class="abs day-box" style="top:241px">Tuesday</div>
  <div class="abs day-box" style="top:359px">Wednesday</div>
  <div class="abs day-box" style="top:476px">Thursday</div>
  <div class="abs day-box" style="top:595px">Friday</div>
</section>

<section class="page page--daily">
  <h2 class="abs heading" style="left:36px;top:118px">During The Day</h2>
  <span class="abs label" style="left:140px;top:160px">Daily Timline</span>
  <span class="abs label" style="left:376px;top:160px">Reminders</span>

  <div class="abs slot" style="top:195px">8am</div>
  <span class="abs hour" style="top:236px">9am</span>
  <div class="abs slot" style="top:272px">10am</div>
  <span class="abs hour" style="top:313px">11am</span>
  <div class="abs slot" style="top:350px">12pm</div>
  <span class="abs hour" style="top:390px">1pm</span>
  <div class="abs slot" style="top:427px">2pm</div>
  <span class="abs hour" style="top:467px">3pm</span>
  <div class="abs slot" style="top:504px">4pm</div>
  <span class="abs hour" style="top:544px">5pm</span>
  <div class="abs slot" style="top:581px">6pm</div>
  <span class="abs hour" style="top:621px">7pm</span>
  <div class="abs slot" style="top:657px">8pm</div>

  <div class="abs rule" style="left:272px;width:208px;top:209px"></div>
  <div class="abs rule" style="left:272px;width:208px;top:235px"></div>
  <div class="abs rule" style="left:272px;width:208px;top:262px"></div>
  <div class="abs rule" style="left:272px;width:208px;top:289px"></div>
  <div class="abs rule" style="left:272px;width:208px;top:316px"></div>
  <div class="abs rule" style="left:272px;width:208px;top:342px"></div>
  <div class="abs rule" style="left:272px;width:208px;top:365px"></div>
  <div class="abs rule" style="left:272px;width:208px;top:391px"></div>

  <span class="abs label" style="left:376px;top:425px">Today lessons</span>
  <div class="abs rule" style="left:272px;width:208px;top:480px"></div>
  <div class="abs rule" style="left:272px;width:208px;top:507px"></div>
  <div class="abs rule" style="left:272px;width:208px;top:534px"></div>
  <div class="abs rule" style="left:272px;width:208px;top:560px"></div>
  <div class="abs rule" style="left:272px;width:208px;top:587px"></div>
  <div class="abs rule" style="left:272px;width:208px;top:614px"></div>
  <div class="abs rule" style="left:272px;width:208px;top:640px"></div>
  <div class="abs rule" style="left:272px;width:208px;top:667px"></div>
  <div class="abs rule" style="left:272px;width:208px;top:694px"></div>
</section>

</body>
</html>
```